Hi,

I am in desperate need of Wordpress website template for for my consulting company. All the graphics are already there, but I need someone who can code that into an extremely nice template for Wordpress (latest version 3.8.1)

I specialize in Consulting and Advise on global software delivery, with a special focus on how to secure innovation within the global delivery platform. I do have the logo and visual identity.

```html
<!DOCTYPE html>
<html lang="en">
<head>
<meta charset="utf-8">
<title>Veltrana</title>
<link rel="stylesheet" href="https://fonts.googleapis.com/css2?family=Questrial&family=Lato:wght@400;700&family=Montserrat:wght@700;800&display=swap">
<style>
:root{
  --header-blue:#1f5b83;
  --header-blue-dark:#174a6d;
  --orange:#f8a81f;
  --orange-deep:#d97f0c;
  --sky:#2ea3e6;
  --ink:#222222;
  --text:#3a3a3a;
  --muted:#6d6d6d;
  --link:#1a8fd6;
  --title-blue:#1a9be0;
  --footer:#17173f;
  --white:#ffffff;
  --line:#e2e2e2;
  --red-link:#c40d0d;
}
*{box-sizing:border-box;margin:0;padding:0}
html,body{width:886px;height:1200px;overflow:hidden;background:var(--white)}
body{position:relative;font-family:"Lato",sans-serif;color:var(--text)}
.abs{position:absolute}

/* Header */
.site-header{position:absolute;left:0;top:0;width:886px;height:145px;background:linear-gradient(180deg,var(--header-blue) 0%,var(--header-blue-dark) 100%)}
.brand{position:absolute;left:34px;top:90px;display:flex;align-items:center;gap:10px}
.brand-mark{width:22px;height:22px;border-radius:50%;background:var(--white)}
.brand-name{font-family:"Questrial",sans-serif;font-size:24px;line-height:1;color:var(--white)}
.main-nav{position:absolute;top:4px;left:434px;display:flex;font-family:"Questrial",sans-serif;font-size:14px}
.main-nav a{display:block;height:29px;line-height:29px;padding:0 14px;color:var(--white);text-decoration:none}
.main-nav a.active{background:var(--white);color:var(--header-blue)}
.search{position:absolute;left:642px;top:98px;width:184px;height:27px;background:var(--white);font-size:11px;color:#777;padding:7px 10px}
.search svg{position:absolute;right:5px;top:3px}

/* Hero */
.hero{position:absolute;left:0;top:145px;width:886px;height:245px;background:linear-gradient(90deg,var(--orange) 0%,#f3a01a 50%,var(--orange-deep) 100%);border-bottom:4px solid #f29a12}
.hero-title{position:absolute;left:35px;top:36px;font-family:"Montserrat",sans-serif;font-weight:800;font-size:22px;line-height:27px;color:var(--white);text-shadow:1px 1px 1px rgba(0,0,0,.35)}
.hero-text{position:absolute;left:38px;top:100px;width:460px;font-size:12px;line-height:18px;color:#1e1a12}
.btn-learn{position:absolute;left:40px;top:172px;width:152px;height:39px;background:linear-gradient(180deg,#fbfbf0,#d8d6c2);border:1px solid #b9b59c;font-family:"Questrial",sans-serif;font-size:19px;color:#444;text-align:center;line-height:37px}
.hero-photo{position:absolute;left:535px;top:0;width:280px;height:241px;background:linear-gradient(180deg,#e69a2a 0%,#8a6a46 45%,#2b3144 75%,#1f2433 100%);opacity:.6}

/* Blue intro banner */
.intro-banner{position:absolute;left:23px;top:408px;width:832px;height:102px}
.intro-title{position:absolute;left:10px;top:31px;font-family:"Montserrat",sans-serif;font-weight:800;font-size:27px;color:var(--white);white-space:nowrap;text-shadow:1px 1px 1px rgba(0,0,0,.3)}
.intro-note{position:absolute;left:544px;top:12px;width:280px;font-size:10.5px;line-height:13.5px;color:#2a2310}
.intro-note p+p{margin-top:14px}

/* Welcome */
.welcome-tab{position:absolute;left:23px;top:524px;width:474px;height:53px;background:var(--ink);color:var(--white);font-family:"Questrial",sans-serif;font-size:31px;line-height:53px;padding-left:7px}
.welcome-box{position:absolute;left:23px;top:577px;width:832px;height:191px;border:1px solid var(--line)}
.welcome-copy{position:absolute;left:4px;top:16px;width:590px;font-size:10.5px;line-height:13.5px;color:var(--text)}
.welcome-copy p{margin-bottom:13px}
.read-more{font-size:9px;color:var(--link);text-decoration:none}
.welcome-photo{position:absolute;left:627px;top:13px;width:191px;height:165px;background:linear-gradient(135deg,#e2a876,#c98448 70%,#8a5a34)}

/* Features */
.feature{position:absolute;top:799px;width:226px}
.feature-photo{width:226px;height:90px;border:1px solid #d0d0d0;padding:4px;background:var(--white)}
.feature-photo div{width:100%;height:100%}
.feature h3{font-family:"Questrial",sans-serif;font-weight:400;font-size:17px;color:var(--title-blue);text-align:center;margin-top:9px}
.feature p{font-size:10.5px;line-height:15px;color:var(--muted);margin-top:6px}
.feature .read-more{display:block;margin-top:16px}

/* Packages band */
.packages-band{position:absolute;left:23px;top:1036px;width:832px;height:62px}
.packages-title{position:absolute;left:18px;top:15px;font-family:"Montserrat",sans-serif;font-weight:800;font-size:24px;color:var(--white);white-space:nowrap;text-shadow:1px 1px 1px rgba(0,0,0,.35)}
.packages-text{position:absolute;left:400px;top:11px;width:400px;text-align:center;font-family:"Questrial",sans-serif;font-size:14px;line-height:18px;color:#2a2310}
.packages-text a{color:var(--red-link);text-decoration:none}

/* Footer */
.site-footer{position:absolute;left:0;top:1122px;width:886px;height:78px;background:var(--footer);color:var(--white);font-family:"Questrial",sans-serif}
.footer-nav{position:absolute;left:36px;top:20px;font-size:14px;display:flex}
.footer-nav a{color:var(--white);text-decoration:none}
.footer-nav span{margin:0 16px}
.copyright{position:absolute;left:36px;top:45px;font-size:10.5px}
.social{position:absolute;left:692px;top:27px;display:flex;gap:10px}
.social span{width:22px;height:22px;display:block}
</style>
</head>
<body>

<header class="site-header">
  <div class="brand">
    <span class="brand-mark"></span>
    <span class="brand-name">veltrana</span>
  </div>
  <nav class="main-nav">
    <a class="active" href="#">HOME</a>
    <a href="#">ABOUT</a>
    <a href="#">SERVICES</a>
    <a href="#">PACKAGES</a>
    <a href="#">CONTACT</a>
  </nav>
  <div class="search">Search
    <svg width="22" height="21" viewBox="0 0 22 21"><circle cx="9" cy="9" r="6.5" fill="none" stroke="#9a9a9a" stroke-width="2"/><line x1="13.5" y1="13.5" x2="20" y2="19.5" stroke="#9a9a9a" stroke-width="3" stroke-linecap="round"/></svg>
  </div>
</header>

<section class="hero">
  <h1 class="hero-title">SECURE INNOVATION WITHIN<br>THE GLOBAL DELIVERY PLATFORM</h1>
  <p class="hero-text">An Online Strategic Plan is a lot like a business plan. You define look at your business, define your values, look at your competitors and think and talk to your customers to determine what you should do to improve your current situation.</p>
  <div class="btn-learn">Learn More</div>
  <div class="hero-photo" role="img" aria-label="Smiling consultant in a dark suit pointing upward"></div>
</section>

<section class="intro-banner">
  <svg class="abs" style="left:0;top:0" width="832" height="102" viewBox="0 0 832 102">
    <polygon points="0,0 498,0 510,51 498,102 0,102" fill="#2ea3e6"/>
    <polygon points="504,0 832,0 832,102 504,102 516,51" fill="#f8a81f"/>
  </svg>
  <h2 class="intro-title">LOREL IPSUM DOLOR SIT AMET</h2>
  <div class="intro-note">
    <p>Do you know what content is converting your visitors or worse, which content is driving them away!</p>
    <p>We work with you to develop strategies to identify this information, that allows you to optimise your content for your visitor’s preferences.</p>
  </div>
</section>

<h2 class="welcome-tab">WELCOME TO VELTRANA</h2>
<section class="welcome-box">
  <div class="welcome-copy">
    <p>Nullam commodo vitae eros ac ornare. Suspendisse rhoncus erat tristique libero rutrum, sodales tempor diam gravida. Praesent quis tincidunt urna. Suspendisse potenti. Nullam est metus, lobortis sed fermentum quis, fermentum congue nibh. Cum sociis natoque penatibus et magnis dis parturient montes, nascetur ridiculus mus.</p>
    <p>Cras vitae sapien viverra massa rhoncus varius. Fusce semper euismod arcu. Praesent ligula risus, scelerisque quis dui sit amet, porttitor feugiat ante. Nullam sodales vestibulum tellus in dictum. Mauris ut massa turpis.</p>
    <p>Proin sed ligula pharetra, facilisis libero in, sagittis ipsum. Duis tincidunt leo ipsum, et elementum ipsum scelerisque id. In vitae pharetra augue, faucibus faucibus est.</p>
    <a class="read-more" href="#">Read More</a>
  </div>
  <div class="welcome-photo" role="img" aria-label="Smiling businesswoman with glasses holding a pen"></div>
</section>

<article class="feature" style="left:42px">
  <div class="feature-photo"><div role="img" aria-label="Team meeting around a conference table" style="background:linear-gradient(90deg,#5b5f66,#c9ccd0 60%,#7b7e84)"></div></div>
  <h3>Our Mission</h3>
  <p>Here is our mission statement. Fusce con se quat congue nisl posuere scelerisque. Aen&nbsp; ean sit amet eros ac dui gravida rutr um.</p>
  <a class="read-more" href="#">Read More</a>
</article>
<article class="feature" style="left:327px">
  <div class="feature-photo"><div role="img" aria-label="Group of business people standing in front of a world map" style="background:linear-gradient(180deg,#8a8d92,#3e3f44)"></div></div>
  <h3>Our Vision</h3>
  <p>Here is our mission statement. Fusce con se quat congue nisl posuere scelerisque. Aen&nbsp; ean sit amet eros ac dui gravida rutr um.</p>
  <a class="read-more" href="#">Read More</a>
</article>
<article class="feature" style="left:607px">
  <div class="feature-photo"><div role="img" aria-label="Binary digits seen through a magnifying glass" style="background:linear-gradient(90deg,#2bb7c9,#79d69a 50%,#2aa4c4)"></div></div>
  <h3>Our Services</h3>
  <p>Here is our mission statement. Fusce con se quat congue nisl posuere scelerisque. Aen&nbsp; ean sit amet eros ac dui gravida rutr um.</p>
  <a class="read-more" href="#">Read More</a>
</article>

<section class="packages-band">
  <svg class="abs" style="left:0;top:0" width="832" height="62" viewBox="0 0 832 62">
    <rect width="832" height="62" fill="#f8a81f"/>
    <polygon points="330,0 350,0 375,31 350,62 330,62 355,31" fill="#ffffff"/>
  </svg>
  <h2 class="packages-title">VIEW OUR PACKAGES</h2>
  <p class="packages-text">Ready to sign up and change the way you think about your website <a href="#">click here to view our packages</a></p>
</section>

<footer class="site-footer">
  <nav class="footer-nav">
    <a href="#">HOME</a><span>|</span><a href="#">ABOUT US</a><span>|</span><a href="#">SERVICES</a><span>|</span><a href="#">CONTACT</a>
  </nav>
  <p class="copyright">© 2014, All Rights Reserved, Veltrana</p>
  <div class="social">
    <span style="background:#3b5998"></span>
    <span style="background:#3a9fd8"></span>
    <span style="background:#d4462f"></span>
    <span style="background:#c4221b"></span>
    <span style="background:#f07a1c"></span>
  </div>
</footer>

</body>
</html>
```